Bright Prospect Hub

I would like 4 different size banner ads. The "Standard" online sizes. I believe they are: 125x125 | 728x90 | 468x60 | 250x250 These banners will be for promoting the website. I want to make sure you can read what the banners say so NO real fancy text. I've uploaded a few ideas as I do want them to kinda look like the website. https://www.brightprospecthub.com/ Take a look at the site and you will see we use money bags, dollar signs and bright colors.

```html
<!DOCTYPE html>
<html lang="en">
<head>
<meta charset="utf-8">
<title>Bright Prospect Hub – Banner Set</title>
<link rel="stylesheet" href="https://fonts.googleapis.com/css2?family=Cherry+Swash:wght@700&family=Poppins:wght@600&display=swap">
<style>
  :root {
    --board: #f8ec3a;
    --blue-deep: #0a5cf2;
    --blue-mid: #0a86f7;
    --cyan: #00e6f6;
    --cyan-text: #3cf0ff;
    --white: #ffffff;
    --swoosh: #ffe600;
    --gold-light: #ffd89a;
    --gold-dark: #e89a3c;
    --sack-light: #f6dfa0;
    --sack-dark: #c9a25a;
    --label: #111111;
  }
  * { box-sizing: border-box; margin: 0; padding: 0; }
  html, body { width: 1200px; height: 823px; overflow: hidden; background: var(--board); }
  .board { position: relative; width: 1200px; height: 823px; }

  .banner {
    position: absolute;
    overflow: hidden;
    background: linear-gradient(120deg, var(--blue-mid) 0%, var(--blue-deep) 50%, var(--blue-mid) 80%, var(--cyan) 100%);
    font-family: "Cherry Swash", Georgia, serif;
    color: var(--white);
  }
  .banner-shadow {
    position: absolute;
    height: 14px;
    background: radial-gradient(ellipse at 50% 0%, rgba(120,100,0,.55) 0%, rgba(120,100,0,0) 70%);
  }
  .bands { position: absolute; inset: 0; width: 100%; height: 100%; }

  .art { position: absolute; }
  .art-dollar { background: linear-gradient(160deg, var(--gold-light), var(--gold-dark)); border-radius: 8px; opacity: .92; }
  .art-sacks { background: linear-gradient(170deg, var(--sack-light), var(--sack-dark)); border-radius: 40% 40% 14px 14px; opacity: .92; }

  .title { position: absolute; left: 0; right: 0; text-align: center; font-weight: 700; line-height: 1; white-space: nowrap; }
  .tagline { position: absolute; text-align: center; font-weight: 700; line-height: 1; white-space: nowrap; }
  .tagline .accent { color: var(--cyan-text); position: relative; }
  .swoosh { position: absolute; left: 0; width: 100%; overflow: visible; }

  .size-label {
    position: absolute;
    font-family: "Poppins", Arial, sans-serif;
    font-weight: 600;
    color: var(--label);
    transform: translateX(-50%);
    white-space: nowrap;
  }

  /* 125 x 125 */
  .banner-125 { left: 40px; top: 53px; width: 197px; height: 197px; }
  .banner-125 .title-a { top: 56px; font-size: 26px; }
  .banner-125 .title-b { top: 86px; font-size: 28px; }
  .banner-125 .tagline { left: 0; right: 0; top: 118px; font-size: 10px; }
  .banner-125 .swoosh { top: 10px; height: 6px; }

  /* 250 x 250 */
  .banner-250 { left: 334px; top: 30px; width: 242px; height: 242px; }
  .banner-250 .title { top: 170px; font-size: 23px; }
  .banner-250 .tagline { left: 0; right: 0; top: 199px; font-size: 11px; }
  .banner-250 .swoosh { top: 11px; height: 6px; }

  /* 468 x 60 */
  .banner-468 { left: 34px; top: 365px; width: 901px; height: 116px; }
  .banner-468 .title { left: 230px; right: 230px; top: 22px; font-size: 38px; }
  .banner-468 .tagline { left: 230px; right: 230px; top: 70px; font-size: 19px; }
  .banner-468 .swoosh { top: 20px; height: 10px; }

  /* 728 x 90 */
  .banner-728 { left: 40px; top: 586px; width: 1114px; height: 138px; }
  .banner-728 .title { left: 280px; right: 280px; top: 26px; font-size: 48px; }
  .banner-728 .tagline { left: 280px; right: 280px; top: 84px; font-size: 24px; }
  .banner-728 .swoosh { top: 25px; height: 12px; }
</style>
</head>
<body>
<main class="board">

  <!-- 125 x 125 -->
  <section class="banner banner-125">
    <svg class="bands" viewBox="0 0 197 197" preserveAspectRatio="none" aria-hidden="true">
      <circle cx="150" cy="20" r="110" fill="#1a9bff" opacity=".25"/>
      <polygon points="197,150 197,197 140,197" fill="#2fd0ff" opacity=".7"/>
    </svg>
    <div class="title title-a">Bright</div>
    <div class="title title-b">Prospect Hub</div>
    <div class="tagline">Plus, A <span class="accent">Monthly Residual<svg class="swoosh" viewBox="0 0 100 10" preserveAspectRatio="none" aria-hidden="true"><path d="M4 9 Q8 2 40 3 Q55 4 70 8" stroke="var(--swoosh)" stroke-width="2" fill="none" stroke-linecap="round"/></svg></span> Income!</div>
  </section>
  <div class="banner-shadow" style="left:50px;top:250px;width:177px;"></div>
  <div class="size-label" style="left:139px;top:270px;font-size:23px;">125 x 125</div>

  <!-- 250 x 250 -->
  <section class="banner banner-250">
    <svg class="bands" viewBox="0 0 242 242" preserveAspectRatio="none" aria-hidden="true">
      <circle cx="180" cy="40" r="140" fill="#22a8ff" opacity=".25"/>
      <polygon points="242,200 242,242 190,242" fill="#2fd0ff" opacity=".7"/>
    </svg>
    <div class="art art-dollar" role="img" aria-label="Golden 3D dollar signs" style="left:29px;top:70px;width:62px;height:78px;"></div>
    <div class="art art-sacks" role="img" aria-label="Three money bags with dollar signs" style="left:106px;top:50px;width:110px;height:96px;"></div>
    <div class="title">Bright Prospect Hub</div>
    <div class="tagline">Plus, A <span class="accent">Monthly Residual<svg class="swoosh" viewBox="0 0 100 10" preserveAspectRatio="none" aria-hidden="true"><path d="M4 9 Q8 2 40 3 Q55 4 70 8" stroke="var(--swoosh)" stroke-width="2" fill="none" stroke-linecap="round"/></svg></span> Income!</div>
  </section>
  <div class="banner-shadow" style="left:345px;top:272px;width:220px;"></div>
  <div class="size-label" style="left:451px;top:295px;font-size:23px;">250 x 250</div>

  <!-- 468 x 60 -->
  <section class="banner banner-468">
    <svg class="bands" viewBox="0 0 901 116" preserveAspectRatio="none" aria-hidden="true">
      <polygon points="0,0 105,0 20,116 0,116" fill="var(--cyan)" opacity=".85"/>
      <polygon points="140,0 195,0 110,116 55,116" fill="var(--cyan)" opacity=".85"/>
      <polygon points="820,0 901,0 901,116 740,116" fill="#22c8ff" opacity=".8"/>
      <polygon points="610,0 680,0 620,116 560,116" fill="#3a8dff" opacity=".25"/>
    </svg>
    <div class="art art-dollar" role="img" aria-label="Golden 3D dollar signs" style="left:98px;top:6px;width:82px;height:104px;"></div>
    <div class="title">Bright Prospect Hub</div>
    <div class="tagline">Plus, A <span class="accent">Monthly Residual<svg class="swoosh" viewBox="0 0 100 10" preserveAspectRatio="none" aria-hidden="true"><path d="M4 9 Q8 2 40 3 Q55 4 70 8" stroke="var(--swoosh)" stroke-width="2" fill="none" stroke-linecap="round"/></svg></span> Income!</div>
    <div class="art art-sacks" role="img" aria-label="Three money bags with dollar signs" style="left:675px;top:2px;width:124px;height:104px;"></div>
    <div class="art art-sacks" role="img" aria-label="Large blurred money bag" style="left:840px;top:0;width:70px;height:116px;opacity:.75;"></div>
  </section>
  <div class="banner-shadow" style="left:80px;top:481px;width:810px;height:30px;"></div>
  <div class="size-label" style="left:509px;top:508px;font-size:23px;">468 x 60</div>

  <!-- 728 x 90 -->
  <section class="banner banner-728">
    <svg class="bands" viewBox="0 0 1114 138" preserveAspectRatio="none" aria-hidden="true">
      <polygon points="0,0 160,0 60,138 0,138" fill="var(--cyan)" opacity=".85"/>
      <polygon points="200,0 265,0 165,138 100,138" fill="var(--cyan)" opacity=".85"/>
      <polygon points="1030,0 1114,0 1114,138 940,138" fill="#22c8ff" opacity=".8"/>
      <polygon points="760,0 840,0 770,138 690,138" fill="#3a8dff" opacity=".25"/>
    </svg>
    <div class="art art-dollar" role="img" aria-label="Blurred golden dollar sign" style="left:0;top:8px;width:40px;height:70px;opacity:.6;"></div>
    <div class="art art-dollar" role="img" aria-label="Golden 3D dollar signs" style="left:150px;top:4px;width:96px;height:124px;"></div>
    <div class="title">Bright Prospect Hub</div>
    <div class="tagline">Plus, A <span class="accent">Monthly Residual<svg class="swoosh" viewBox="0 0 100 10" preserveAspectRatio="none" aria-hidden="true"><path d="M4 9 Q8 2 40 3 Q55 4 70 8" stroke="var(--swoosh)" stroke-width="2" fill="none" stroke-linecap="round"/></svg></span> Income!</div>
    <div class="art art-sacks" role="img" aria-label="Three money bags with dollar signs" style="left:840px;top:2px;width:142px;height:126px;"></div>
    <div class="art art-sacks" role="img" aria-label="Large blurred money bag" style="left:1040px;top:0;width:80px;height:138px;opacity:.75;"></div>
  </section>
  <div class="banner-shadow" style="left:90px;top:724px;width:1010px;height:34px;"></div>
  <div class="size-label" style="left:605px;top:750px;font-size:23px;">728 x 90</div>

</main>
</body>
</html>
```